The Wardrobe Sage needs a business card

The wardrobe sage is a lead generation service serving the Custom Closet industry.

Here is the basic card information:

The Wardrobe Sage
Dorian Pettigrew
Owner/CEO
Charlotte, NC
704-318-5527 Cell
Email: dpettigrew@TheWardrobeSage.com

Additional information for the card:

"High quality, flat rate lead generation exclusively for the custom closet industry"

Bullet points for the back:

- Low fixed cost
- Easy to budget
- Guaranteed qualified Leeds
- Exclusivity per city

Logo attached, head shot attached. Photos of closet systems attached

```html
<!DOCTYPE html>
<html lang="en">
<head>
<meta charset="utf-8">
<title>The Wardrobe Sage – Business Card</title>
<link href="https://fonts.googleapis.com/css2?family=Tinos:ital,wght@0,400;0,700;1,400&family=Parisienne&display=swap" rel="stylesheet">
<style>
  :root {
    --brown: #9b5f2c;
    --brown-dark: #84501f;
    --ink: #4a4a4a;
    --paper: #ffffff;
    --stage: #ebe6df;
    --rule: rgba(255,255,255,0.55);
  }
  * { margin: 0; padding: 0; box-sizing: border-box; }
  html, body { width: 900px; height: 1200px; overflow: hidden; }
  body {
    background: var(--stage);
    font-family: "Tinos", "Times New Roman", serif;
    position: relative;
  }
  .card {
    position: absolute;
    left: 80px;
    width: 737px;
    height: 428px;
    border-radius: 18px;
    overflow: hidden;
    box-shadow: 0 8px 18px rgba(0,0,0,0.35);
  }
  .card--front { top: 125px; background: var(--paper); }
  .card--back { top: 637px; background: var(--paper); }

  /* Front */
  .closet-photo {
    position: absolute;
    left: 0; top: 0;
    width: 737px; height: 375px;
    background: linear-gradient(135deg, #f4efe9 0%, #e6ddd2 45%, #d9cbbb 100%);
    clip-path: polygon(260px 0, 737px 0, 737px 375px, 400px 375px, 400px 175px);
  }
  .portrait {
    position: absolute;
    left: 404px; top: 20px;
    width: 270px; height: 355px;
    background: linear-gradient(180deg, #c89a7c 0%, #b58468 25%, #34415a 45%, #26324a 100%);
    border-radius: 120px 120px 8px 8px;
  }
  .brand-name {
    position: absolute;
    left: 40px; top: 118px;
    width: 280px;
    text-align: center;
    color: var(--ink);
    font-size: 34px;
    font-weight: 400;
    line-height: 1.1;
  }
  .person-name {
    position: absolute;
    left: 38px; top: 214px;
    color: var(--ink);
    font-size: 25px;
    font-weight: 700;
  }
  .person-title {
    position: absolute;
    left: 38px; top: 245px;
    color: var(--brown);
    font-size: 17px;
  }
  .contact-list {
    position: absolute;
    left: 38px; top: 281px;
    list-style: none;
    color: var(--ink);
    font-size: 15.5px;
  }
  .contact-list li {
    display: flex;
    align-items: center;
    height: 23px;
  }
  .contact-list svg { width: 13px; height: 13px; margin-right: 9px; fill: var(--brown); }
  .tagline-band {
    position: absolute;
    left: 0; bottom: 0;
    width: 737px; height: 53px;
    background: var(--brown);
    display: flex;
    align-items: center;
    justify-content: center;
  }
  .tagline {
    font-family: "Parisienne", cursive;
    color: #fff;
    font-size: 21px;
    letter-spacing: 0.2px;
  }

  /* Back */
  .back-panel {
    position: absolute;
    left: 0; top: 0;
    width: 358px; height: 428px;
    background: var(--brown);
  }
  .brand-name--light {
    position: absolute;
    left: 20px; top: 110px;
    width: 318px;
    text-align: center;
    color: #fff;
    font-size: 36px;
    line-height: 1.1;
  }
  .benefits {
    position: absolute;
    left: 44px; top: 238px;
    width: 264px;
    list-style: none;
    color: #fff;
    font-size: 19px;
  }
  .benefits li {
    height: 38.5px;
    display: flex;
    align-items: center;
    border-bottom: 1px solid var(--rule);
    padding-left: 24px;
    position: relative;
  }
  .benefits li:last-child { border-bottom: none; }
  .benefits li::before {
    content: "";
    position: absolute;
    left: 1px; top: 50%;
    width: 10px; height: 10px;
    margin-top: -5px;
    border-radius: 50%;
    background: #fff;
  }
  .closet-gallery {
    position: absolute;
    left: 371px; top: 26px;
    width: 334px;
  }
  .gallery-shot {
    width: 334px;
    height: 184px;
    margin-bottom: 11px;
  }
  .gallery-shot--walkin {
    background: linear-gradient(180deg, #d8cfc4 0%, #a57753 45%, #6e4a34 75%, #d9d2c8 100%);
  }
  .gallery-shot--reachin {
    background: linear-gradient(90deg, #eeeeee 0%, #c7935f 20%, #e7ddd2 50%, #c7935f 80%, #eeeeee 100%);
  }
</style>
</head>
<body>

  <section class="card card--front">
    <div class="closet-photo" role="img" aria-label="Bright luxury walk-in closet with shelves of handbags and shoes"></div>
    <div class="portrait" role="img" aria-label="Head shot of the owner in a plaid blazer, arms crossed"></div>

    <div class="brand-name">The Wardrobe Sage</div>

    <h1 class="person-name">Dorian Pettigrew</h1>
    <p class="person-title">Owner/CEO</p>

    <ul class="contact-list">
      <li>
        <svg viewBox="0 0 24 24" aria-hidden="true"><path d="M6.6 10.8a15.1 15.1 0 0 0 6.6 6.6l2.2-2.2a1 1 0 0 1 1-.25 11.4 11.4 0 0 0 3.6.57 1 1 0 0 1 1 1V20a1 1 0 0 1-1 1A17 17 0 0 1 3 4a1 1 0 0 1 1-1h3.5a1 1 0 0 1 1 1c0 1.25.2 2.45.57 3.57a1 1 0 0 1-.25 1z"/></svg>
        704-318-5527 Cell
      </li>
      <li>
        <svg viewBox="0 0 24 24" aria-hidden="true"><path d="M2 5h20v14H2z M2 5l10 8 10-8" stroke="#fff" stroke-width="1.5"/></svg>
        dpettigrew@TheWardrobeSage.com
      </li>
      <li>
        <svg viewBox="0 0 24 24" aria-hidden="true"><path d="M12 2a7 7 0 0 0-7 7c0 5.2 7 13 7 13s7-7.8 7-13a7 7 0 0 0-7-7zm0 9.5A2.5 2.5 0 1 1 12 6.5a2.5 2.5 0 0 1 0 5z"/></svg>
        Charlotte, NC
      </li>
    </ul>

    <div class="tagline-band">
      <p class="tagline">High quality, flat rate lead generation exclusively for the custom closet industry</p>
    </div>
  </section>

  <section class="card card--back">
    <div class="back-panel">
      <div class="brand-name--light">The Wardrobe Sage</div>
      <ul class="benefits">
        <li>Low fixed cost</li>
        <li>Easy to budget</li>
        <li>Guaranteed qualified Leeds</li>
        <li>Exclusivity per city</li>
      </ul>
    </div>
    <div class="closet-gallery">
      <div class="gallery-shot gallery-shot--walkin" role="img" aria-label="Warm wood walk-in closet with hanging clothes and a blue armchair"></div>
      <div class="gallery-shot gallery-shot--reachin" role="img" aria-label="Reach-in wood closet system with white drawers behind sliding barn doors"></div>
    </div>
  </section>

</body>
</html>
```